2 Fold Brochure

We are a spa looking to create a professional elegant two fold brochure for a spa mainly black and white with a splash of lime green.
Look and feel: chic, modern, and spa-ish.

The front will include an image and also it should say: (somewhere under the photo) wherever you think it will look nice.
Skin Tightening
Cellulite Reduction
Body Contouring

The second Page:
Bipolar Radiofrequency(bolded): for immediate face lifting, tone and a complete new younger looking skin!
Multipolar Radiofrequency(bolded): with Vacuum system for body contour, cellulite and fat detachment from adipose tissue.
Cavitation with red LED to treat face and small areas of the body. Red LED light stimulates collagen synthesis.

Ultra Cavitation will sculpt, treat fat, cellulite and improve body shape! It does NOT involve surgery. There is no need for anesthesia, hospital stay or time off from work. Ultra cavitation will promote microscopic air bubbles to surround the lipocyte(fat cell) membranes and with its resonant frequency, the bubbles cause a high enough pressure to break up fat instantly. These broken lipocytes are then safely metabolized out of the human body.

PRESSOTHERAPY: A Complete Body Detox! Pressortherapy based on air pressure, promotes lymphatic drainage. It aslo has infrared system for body heat and electro muscle stimulation system.

Third Page:
Packages:

1. THE NEW FACELIFT:
*Skin Tightening
*Wrinkle Reduction
*Dark Circle Elimination
*Puffy Eye Relief

BODY SHAPING

2. BODY
*Fat Reduction
*Cellulite Reduction
*Body Firming

3. PRESSOTHERAPY (DETOX) $85
*Toxic Flushing
*Lymphatic Drainage
*Toning

5.POST PREGNANCY
*Fat Reduction
*Tummy Firming and Toning
*Cellulite Reduction
*Butt Toning

Buy 5 get 1 Free - $1,250
Buy 10 get 2 Free- $2,500

The back of the second page will include before and after photos I will be sending later. Also include the Logo in the front and by the prices. I have attached our logo.

Also we need a photo to place in the front. Something that shows face and body fat reduction.

```html
<!DOCTYPE html>
<html lang="en">
<head>
<meta charset="utf-8">
<title>Lumen Day Spa – Package Services</title>
<link href="https://fonts.googleapis.com/css2?family=Source+Sans+3:wght@400;600&display=swap" rel="stylesheet">
<style>
  :root {
    --page: #f1f1f1;
    --lime: #a6e22a;
    --lime-light: #c4f05a;
    --ink: #1e1e1e;
    --heading: #a8a8a8;
    --rule: #9a9a9a;
    --ring: #d9d9d9;
    --white: #ffffff;
  }
  html, body { margin: 0; padding: 0; overflow: hidden; }
  body { background: var(--page); }
  .brochure-page {
    position: relative;
    width: 840px;
    height: 1200px;
    overflow: hidden;
    background: var(--page);
    font-family: "Source Sans 3", Arial, sans-serif;
    color: var(--ink);
  }
  .backdrop { position: absolute; inset: 0; }
  .brand-badge {
    position: absolute;
    left: 600px; top: 6px;
    width: 134px; height: 134px;
    border-radius: 50%;
    background: var(--white);
    box-shadow: 0 0 0 8px var(--ring);
    display: flex; align-items: center; justify-content: center;
    text-align: center;
  }
  .brand-name {
    font-size: 19px; font-weight: 600; line-height: 1.1;
    color: var(--ink); letter-spacing: 1px;
  }
  .section-title {
    position: absolute;
    left: 456px;
    margin: 0;
    font-size: 42px; font-weight: 400;
    color: var(--heading);
    text-shadow: 2px 2px 3px rgba(0,0,0,0.5);
  }
  .title-services { top: 320px; }
  .title-deals { top: 858px; }
  .service {
    position: absolute; left: 460px;
    margin: 0; padding: 0; list-style: none;
    font-size: 14px; line-height: 21.4px;
  }
  .service-1 { top: 414px; }
  .service-2 { top: 513px; }
  .service-3 { top: 612px; }
  .service-4 { top: 711px; }
  .price {
    position: absolute; left: 727px;
    font-size: 30px; line-height: 1;
  }
  .price-1 { top: 444px; }
  .price-2 { top: 543px; }
  .price-3 { top: 642px; }
  .price-4 { top: 752px; }
  .rule { position: absolute; width: 1px; background: var(--rule); }
  .rule-services { left: 703px; top: 409px; height: 418px; }
  .rule-deals { left: 656px; top: 933px; height: 100px; }
  .deal { position: absolute; left: 460px; font-size: 14px; }
  .deal-1 { top: 950px; }
  .deal-2 { top: 999px; }
  .deal-price { position: absolute; left: 667px; font-size: 32px; line-height: 1; }
  .deal-price-1 { top: 944px; }
  .deal-price-2 { top: 993px; }
  .intro-copy {
    position: absolute; left: 151px; top: 981px;
    margin: 0; font-size: 13px; line-height: 22.6px;
  }
</style>
</head>
<body>
<main class="brochure-page">
  <svg class="backdrop" width="840" height="1200" viewBox="0 0 840 1200" xmlns="http://www.w3.org/2000/svg">
    <defs>
      <linearGradient id="skinTone" x1="0" y1="0" x2="1" y2="1">
        <stop offset="0" stop-color="#5e3a2a"/>
        <stop offset="0.45" stop-color="#b5815a"/>
        <stop offset="1" stop-color="#8a5a3c"/>
      </linearGradient>
      <linearGradient id="facialTone" x1="0" y1="0" x2="1" y2="1">
        <stop offset="0" stop-color="#f6ebe5"/>
        <stop offset="1" stop-color="#e6c2b0"/>
      </linearGradient>
      <linearGradient id="lilyTone" x1="0" y1="0" x2="1" y2="1">
        <stop offset="0" stop-color="#fbe3ec"/>
        <stop offset="1" stop-color="#e79ab8"/>
      </linearGradient>
      <linearGradient id="portraitTone" x1="0" y1="0" x2="1" y2="1">
        <stop offset="0" stop-color="#fbece6"/>
        <stop offset="1" stop-color="#e8b8a8"/>
      </linearGradient>
    </defs>

    <path class="lime-sweep" d="M0,380 C260,240 560,70 740,0 H840 V1200 H0 Z" fill="var(--lime)"/>
    <path class="lime-highlight" d="M0,470 C280,300 600,110 800,0 H816 C620,120 300,320 0,500 Z" fill="var(--lime-light)"/>
    <path class="hero-photo" role="img" aria-label="Close-up photo of a woman's face with glowing bronze skin" d="M0,0 H800 C600,100 300,260 0,470 Z" fill="url(#skinTone)"/>
    <path class="page-field" d="M840,26 C540,190 290,400 200,620 C158,730 150,950 150,1200 H840 Z" fill="var(--page)"/>

    <g class="photo-circle">
      <circle cx="467" cy="227" r="80" fill="var(--ring)"/>
      <circle cx="467" cy="227" r="72" fill="var(--white)"/>
      <circle cx="467" cy="227" r="66" fill="url(#facialTone)" role="img" aria-label="Photo of a woman receiving a relaxing facial massage"/>
    </g>
    <g class="photo-circle">
      <circle cx="307" cy="440" r="94" fill="var(--ring)"/>
      <circle cx="307" cy="440" r="85" fill="var(--white)"/>
      <circle cx="307" cy="440" r="78" fill="url(#lilyTone)" role="img" aria-label="Photo of a pink lily flower"/>
    </g>
    <g class="photo-circle">
      <circle cx="147" cy="773" r="174" fill="var(--ring)"/>
      <circle cx="147" cy="773" r="163" fill="var(--white)"/>
      <circle cx="147" cy="773" r="154" fill="url(#portraitTone)" role="img" aria-label="Photo of a woman with smooth skin resting her head on her hands"/>
    </g>
  </svg>

  <div class="brand-badge"><span class="brand-name">LUMEN<br>DAY SPA</span></div>

  <h2 class="section-title title-services">Package Services</h2>

  <ul class="service service-1">
    <li>1. THE NEW FACELIFT:</li>
    <li>*Skin Tightening</li>
    <li>*Wrinkle Reduction</li>
    <li>*Dark Circle Elimination</li>
  </ul>
  <ul class="service service-2">
    <li>2. BODY</li>
    <li>*Fat Reduction</li>
    <li>*Cellulite Reduction</li>
    <li>*Body Firming</li>
  </ul>
  <ul class="service service-3">
    <li>3. PRESSOTHERAPY (DETOX)</li>
    <li>*Toxic Flushing</li>
    <li>*Lymphatic Drainage</li>
    <li>*Toning</li>
  </ul>
  <ul class="service service-4">
    <li>4. POST PREGNANCY</li>
    <li>*Fat Reduction</li>
    <li>*Tummy Firming and Toning</li>
    <li>*Cellulite Reduction</li>
    <li>*Butt Toning</li>
  </ul>

  <div class="rule rule-services"></div>
  <span class="price price-1">$$$</span>
  <span class="price price-2">$$$</span>
  <span class="price price-3">$85</span>
  <span class="price price-4">$$$</span>

  <h2 class="section-title title-deals">Package Deals</h2>
  <div class="rule rule-deals"></div>
  <span class="deal deal-1">Buy 5 get 1 Free</span>
  <span class="deal deal-2">Buy 10 get 2 Free</span>
  <span class="deal-price deal-price-1">$1250</span>
  <span class="deal-price deal-price-2">$2500</span>

  <p class="intro-copy">
    Placeholder text Placeholder text Placeholder text<br>
    Placeholder text Placeholder text Placeholder text<br>
    Placeholder text Placeholder text Placeholder text<br>
    Placeholder text Placeholder text Placeholder text<br>
    Placeholder text Placeholder text Placeholder text<br>
    Placeholder text Placeholder text Placeholder text
  </p>
</main>
</body>
</html>
```